依頼詳細
弊社では『自宅でできる郵送検査』サービスを行っております。
ネットで注文した最短翌日には自宅に検査キットが届き、自分で採取しポストから返送。自社登録衛生検査所にて検査をし、検査結果はWEB上にて確認できる。利便性の高いサービスとなっております。
KTR医学検査研究所は2022年で創業25年となります。郵送検査業界の中でも経歴が長く、信頼性の高い検査を行っております。
詳しくはこちらのサイトにて▶ https://www.ktlabo-example.jp/

検査を申込んだお客様は、不安な気持ちで検査キットを受け取るため、少しでも明るい気持ちになって安心できるようなデザインを募集いたします。

現在の箱は信頼性や清潔感を第一としてデザインされております。
※念のため現在使用している箱のデザインを添付しております。
記載項目
【パッケージの作成情報】
下記の3種類を作成していただきます。
デザインは基本統一で、色の違いなどで差異をつけていただきたいです。
①男性用
②女性用
③性別関係なく両方でつかえる用

【サイズ】
表面W220mm X H158mm
裏面W220mm X H158mm
側面W35mm X H158mm
◎展開図aiをデータを添付しておりますので、ダウンロードしてご使用ください。

aiデータはアウトライン前とアウトライン後のデータを納品していただきます。
psdにて背景などを作成した場合にはCMYKカラーの解像度350dpiにて作成ください。

【デザインへの要望】
・清潔感や安心感がある
・検査への信頼感がある
・ポップorナチュラルorおしゃれなど少し今の時代をとりいれている
・模様などは可ですが、イラストは不可とします

なるべくシンプルなのものを希望しますが、要望にそっていれば多少大胆なデザインでも受け付けております。
ロゴや社名は使用してもしなくても、お任せいたします。
ECサイトやLPに配置した際に、見た目が映えるデザインが望ましいです。
希望イメージ
シンプル 複雑
単色 カラフル
暗い 明るい
日常 高級
遊び心 厳粛
未来的 伝統的
女性的 男性的
希望する色
色はお任せします
納品ファイル
• イラストレーター形式 (.ai)
• フォトショップ形式 (.psd)
• PNG形式 (.png)
1/4追記:イラスト不可と記載しておりましたが、イラストも可といたします。よろしくお願いいたします。
大変申し訳ございませんが、選定にお時間をいただいております。今しばらくお待ちくださいませ。
■ 選んだ理由

とてもおしゃれで、性別問わず受け入れられるデザインであることがまず目を引きました。
さらに、お客様が手にとった時に『人に見られてもバレない』『安心感がある』と思っていただけるような配慮がなされており、社員アンケートでもその点がとくに好評でした。
以上をふまえたうえで、従来の検査キットの見た目を払拭できるような素敵なデザインだったため、今回選定させていただきました。

■ 提案者全員のお礼・コメント

この度は弊社の検査キットパッケージに、沢山のデザインをご提案いただきありがとうございました。
ネガティブな商材だからと後ろ向きになりがちなサービスですが、みなさまより素敵なご提案をいただき、とても心が温まりました。
どれも良いものばかりでひとつに絞れず本当に悩んでしまい、選定までにお時間をいただき申し訳ございませんでした。
またクラフティアにてご依頼することもあるかと存じますので、その際にはぜひお力お貸しください。
ありがとうございました。

```html
<!DOCTYPE html>
<html lang="ja">
<head>
<meta charset="utf-8">
<title>KTR医学検査研究所 検査キット パッケージ展開図</title>
<link href="https://fonts.googleapis.com/css2?family=Noto+Sans+JP:wght@500;700&family=Montserrat:wght@700&display=swap" rel="stylesheet">
<style>
  :root {
    --paper: #ffffff;
    --dieline: #9a9a9a;
    --fold: #c4c4c4;
    --lime: #b3d24f;
    --lime-deep: #8cc43c;
    --lime-soft: #c6de73;
    --brand-navy: #1d3f8f;
    --ink: #2a3550;
  }
  html, body {
    margin: 0;
    padding: 0;
    width: 878px;
    height: 1200px;
    overflow: hidden;
    background: var(--paper);
  }
  .dieline-sheet {
    position: absolute;
    inset: 0;
    width: 878px;
    height: 1200px;
  }
  .cut { fill: none; stroke: var(--dieline); stroke-width: 1.2; }
  .fold { fill: none; stroke: var(--fold); stroke-width: 1; }
  .band-top { fill: var(--lime); }
  .band-pattern { fill: url(#patternTone); }
  .brand-name {
    font-family: "Noto Sans JP", sans-serif;
    font-weight: 700;
    font-size: 15px;
    fill: var(--brand-navy);
  }
  .brand-sub {
    font-family: "Montserrat", sans-serif;
    font-weight: 700;
    font-size: 5.5px;
    letter-spacing: 0.6px;
    fill: var(--brand-navy);
  }
  .brand-mark { fill: var(--brand-navy); }
  .front-name {
    font-family: "Noto Sans JP", sans-serif;
    font-weight: 700;
    font-size: 30px;
    fill: var(--brand-navy);
  }
</style>
</head>
<body>
<svg class="dieline-sheet" viewBox="0 0 878 1200" xmlns="http://www.w3.org/2000/svg">
  <defs>
    <linearGradient id="patternTone" x1="0" y1="0" x2="1" y2="1">
      <stop offset="0" stop-color="#a9cf52"/>
      <stop offset="0.5" stop-color="#8cc43c"/>
      <stop offset="1" stop-color="#9fcb48"/>
    </linearGradient>
  </defs>

  <!-- green band: lid section -->
  <rect class="band-top" x="433" y="15" width="313" height="255"/>

  <!-- green band: patterned base section -->
  <rect class="band-pattern" x="433" y="660" width="313" height="496"
        role="img" aria-label="黄緑の円と幾何学的な曲線が重なる装飾パターン"/>

  <!-- outer cut line: lid flap with tabs -->
  <path class="cut" d="M140 181 L140 40 Q140 15 165 15 L720 15 Q746 15 746 40 L746 181"/>
  <path class="cut" d="M140 40 L120 40 L120 15 L140 15"/>
  <path class="cut" d="M746 40 L766 40 L766 15 L746 15"/>

  <!-- left side flap -->
  <path class="cut" d="M140 181 L15 181 L0 196 L0 380 L12 380 L12 420 L0 420 L0 640 L15 655 L140 655"/>
  <path class="fold" d="M0 270 L140 270 M0 638 L140 638"/>
  <!-- right side flap -->
  <path class="cut" d="M746 181 L863 181 L878 196 L878 380 L866 380 L866 420 L878 420 L878 640 L863 655 L746 655"/>
  <path class="fold" d="M746 270 L878 270 M746 638 L878 638"/>

  <!-- lower flaps beside base -->
  <path class="cut" d="M140 655 L140 702 L120 702 L120 720 L140 720"/>
  <path class="cut" d="M746 655 L746 702 L766 702 L766 720 L746 720"/>

  <!-- base panel outline and bottom tabs -->
  <path class="cut" d="M140 720 L140 1156 L180 1156 L190 1185 L260 1185 L270 1156 L616 1156 L626 1185 L696 1185 L706 1156 L746 1156 L746 720"/>

  <!-- fold lines -->
  <path class="fold" d="M140 181 L746 181 M140 270 L746 270 M140 638 L746 638 M140 702 L746 702 M140 181 L140 655 M746 181 L746 655"/>

  <!-- lid brand lockup -->
  <g class="brand-lockup">
    <rect class="brand-mark" x="222" y="204" width="11" height="11"/>
    <text class="brand-name" x="239" y="215">KTR医学検査研究所</text>
    <text class="brand-sub" x="223" y="228">MEDICAL TESTING LABORATORY</text>
  </g>

  <!-- inverted brand lockup on inner wall -->
  <g class="brand-lockup" transform="rotate(180 320 686)">
    <rect class="brand-mark" x="222" y="675" width="11" height="11"/>
    <text class="brand-name" x="239" y="686">KTR医学検査研究所</text>
    <text class="brand-sub" x="223" y="699">MEDICAL TESTING LABORATORY</text>
  </g>

  <!-- front name mark -->
  <text class="front-name" x="288" y="950">KTR</text>
</svg>
</body>
</html>
```